Shopping center investment profile

We need to design a two-page 8.5" x 11" brochure that can be used as a template for profiling our shopping centers and demonstrating our track record to investors.

Our company (Pelvoran Real Estate Investments) owns retail shopping centers in the southwestern United States. Our website is www.kelvistrand.example, but we will be redesigning and modernizing the website and logo in the near future, so please do not use the color schemes or framework of the website for the brochure.

Our investors are institutional and high net worth investors who typically have an existing relationship with our company. They are determining whether to invest multi-millions of dollars in a shopping center opportunity, so the brochure needs to be professional, very high quality and provide key information about the specific property.
Updates

Additional guidance on color scheme:

We would like to see a Blue (something like Hex #5A61BC) and Gold (Hex #EDB215) or (Hex #DDA24B) color scheme with some Black accents 

Thank you!

Target Market(s)

Our target audiences are institutional investors, high net-worth individuals, financial firms and medium to large commercial real estate companies.

Industry/Entity Type

Investment

Requirements
Must have
• Clean and modern look with corresponding fonts and colors.
• Incorporates the information found in the attached "Morrowick Commons profile" Pages or PDF file.
• Final file design files that can be modified easily
Nice to have
• Two examples of industry brochures are attached. These are examples of the professional quality that we are looking for, not necessarily the design or format.

```html
<!DOCTYPE html>
<html lang="en">
<head>
<meta charset="utf-8">
<title>Morrowick Commons – Investment Profile</title>
<link href="https://fonts.googleapis.com/css2?family=Source+Sans+3:wght@400;600&display=swap" rel="stylesheet">
<style>
:root{
  --tan:#EBC48E;
  --orange:#E0A24E;
  --gold:#EDB215;
  --blue:#5A61BC;
  --grey:#C9C9C9;
  --ink:#1a1a1a;
  --white:#ffffff;
}
*{margin:0;padding:0;box-sizing:border-box}
html,body{width:1200px;height:930px;overflow:hidden;background:#fff}
body{font-family:"Source Sans 3",sans-serif;color:var(--ink);position:relative}
.block{position:absolute}
.head{position:absolute;height:43px;padding-left:20px;font-size:27px;line-height:43px;font-weight:400}
.left{left:0;width:602px}
.right{left:602px;width:598px}
.head.left{background:var(--tan)}
.head.right{background:var(--gold);padding-left:30px}
.panel-orange{background:var(--orange)}
.panel-blue{background:var(--blue);color:var(--white)}
.panel-grey{background:var(--grey)}
ul{list-style:none}
.bullets li{font-size:17px;line-height:29.5px;padding-left:14px;text-indent:-10px}
.bullets li::before{content:"• "}
.challenges li{font-size:15.5px;line-height:20px;margin-bottom:8px;padding-right:20px}
.challenges li::before{content:"• "}
.figures{padding:0 30px}
.figures div{display:flex;justify-content:space-between;font-size:14.5px;line-height:25.8px}
.photo{background:linear-gradient(180deg,#5b86c8 0%,#b9c9de 45%,#8a4a38 62%,#6a3a30 80%,#595d66 100%)}
</style>
</head>
<body>

<div class="head left" style="top:0">Opportunity</div>
<div class="block left panel-orange" style="top:43px;height:309px;padding:10px 0 0 20px">
  <ul class="bullets">
    <li>Bank owned property with attractive purchase price</li>
    <li>Strong relationship with seller’s broker and decision makers</li>
    <li>Redevelopment upside with management and leasing</li>
    <li>No major renovations required</li>
    <li>Tarrow location has very strong population, education and income demographics</li>
    <li>Adjacent to premier 2,500-residence master planned community of Vestmere Lakes</li>
    <li>Strong employment area with the new Corvell Gateway hospital and the adjacent Hallister Cancer center</li>
  </ul>
</div>

<div class="head right" style="top:0">Challenges and Solutions</div>
<div class="block right panel-blue" style="top:43px;height:309px;padding:12px 0 0 30px">
  <ul class="challenges">
    <li>Nationwide vacancy rate - Pelvoran did significant due diligence on the property before purchasing the asset, and determined that the location is an A/A-; Tenant improvement and leasing commissions were reserved in order to attract national and regional tenants</li>
    <li>Size of Anchor space - Pelvoran determined that a family-friendly entertainment venue would best serve the demographics in the area instead of another grocer; Pelvoran sought out an experienced operator in Whisker Lane, who has multiple locations in three states</li>
    <li>Curb Appeal - With vacancy and a stigma attached to the center, Pelvoran had to change the center’s appeal to the community. Pelvoran worked hand in hand with the Town of Tarrow and the Vestmere Lakes community association to paint the center, upgrade landscaping and add new and larger monument signs</li>
  </ul>
</div>

<div class="block left photo" style="top:352px;height:296px" role="img" aria-label="Rendering of the renovated shopping center storefronts with signage, trees and parked cars"></div>

<div class="head right" style="top:352px">Summary</div>
<div class="block right panel-grey figures" style="top:395px;height:253px;padding-top:32px">
  <div><span>Property Type</span><span>Shopping Center</span></div>
  <div><span>Size</span><span>79,490 sq ft</span></div>
  <div><span>Purchased</span><span>April 2007</span></div>
  <div><span>Total Investment</span><span>$X,XXX,XXX</span></div>
  <div><span>Purchase Occupancy</span><span>8.39%</span></div>
  <div><span>Current Occupancy</span><span>97.29%</span></div>
  <div><span>Projected 5-year IRR (Unleveraged)</span><span>XX.XX%</span></div>
</div>

<div class="head left" style="top:648px">Results</div>
<div class="block left panel-orange" style="top:691px;height:239px;padding:16px 0 0 20px">
  <ul class="bullets">
    <li>Stabilized the shopping center within three years, producing excellent results for investors</li>
    <li>Transformed the center into a vibrant destination that the surrounding community is excited about</li>
    <li>Transitioned legacy tenants to upgrade the business operators</li>
    <li>Reduced the shopping center’s operating expenses by replacing vendors and appealing property taxes</li>
  </ul>
</div>

<div class="head right" style="top:648px">Investment Information</div>
<div class="block right panel-grey figures" style="top:691px;height:239px;padding-top:8px">
  <div><span>Purchase Price</span><span>$X,XXX,XXX</span></div>
  <div><span>Sponsor Acquisition Fee</span><span>$XX,XXX</span></div>
  <div><span>Painting and Landscape</span><span>$XXX,XXX</span></div>
  <div><span>TI/LC Reserve</span><span>$X,XXX,XXX</span></div>
  <div><span>Operating Expenses</span><span>$XXX,XXX</span></div>
  <div><span>Total Cash Investment</span><span></span></div>
  <div style="margin-top:26px"><span>Investor / Sponsor Split</span><span>XX% / XX%</span></div>
</div>

</body>
</html>
```